Toravel Project Consulting

I need a logo and business card design for a small business operating in the management consulting and contractor space, predominantly in local and state government. I specialise in project management, financial consulting, people and culture, procurement, ICT transformation and contracting for corporate support areas of organisations.

Industry/Entity Type

Business

```html
<!DOCTYPE html>
<html lang="en">
<head>
<meta charset="UTF-8">
<title>Toravel Project Consulting – Business Card</title>
<link rel="stylesheet" href="https://fonts.googleapis.com/css2?family=Questrial&family=Open+Sans:wght@400;600;700&display=swap">
<style>
  :root {
    --page-bg: #e9e9eb;
    --card-bg: #ffffff;
    --brand-blue: #2a7fc4;
    --band-blue: #1f6fb8;
    --text-grey: #4a4a4c;
    --text-dark: #2c2c2e;
    --band-grey: #9a9ca0;
    --band-grey-light: #c9cacd;
  }
  * { box-sizing: border-box; margin: 0; padding: 0; }
  html, body {
    width: 1200px; height: 900px; overflow: hidden;
    background: var(--page-bg);
  }
  .canvas {
    position: relative; width: 1200px; height: 900px;
  }
  .card {
    position: absolute; left: 320px; width: 560px; height: 320px;
    background: var(--card-bg);
    box-shadow: 0 6px 18px rgba(0,0,0,0.18);
    overflow: hidden;
  }
  .card--front { top: 90px; }
  .card--back  { top: 490px; }

  .brand-mark {
    display: block; border-radius: 50%;
    background: var(--brand-blue);
    margin: 0 auto;
  }
  .brand-name {
    font-family: "Questrial", sans-serif;
    color: var(--brand-blue);
    font-weight: 400;
    text-align: center;
    white-space: nowrap;
  }

  .card--front .brand-mark { width: 70px; height: 70px; margin-top: 88px; }
  .card--front .brand-name { font-size: 34px; margin-top: 22px; }

  .card--back .brand-mark { width: 46px; height: 46px; margin-top: 34px; }
  .card--back .brand-name { font-size: 26px; margin-top: 12px; }

  .holder {
    position: absolute; left: 40px; top: 160px;
    font-family: "Open Sans", sans-serif;
  }
  .holder__name { font-weight: 700; font-size: 17px; color: var(--brand-blue); line-height: 1.2; }
  .holder__role { font-style: italic; font-size: 15px; color: var(--text-dark); line-height: 1.2; }

  .divider {
    position: absolute; left: 262px; top: 162px; width: 2px; height: 58px;
    background: linear-gradient(to bottom, rgba(42,127,196,0), var(--brand-blue), rgba(42,127,196,0));
  }

  .contacts {
    position: absolute; left: 290px; top: 158px;
    list-style: none;
    font-family: "Open Sans", sans-serif; font-size: 15px; color: var(--text-dark);
  }
  .contacts li { display: flex; align-items: center; height: 22px; }
  .contacts .icon {
    width: 12px; height: 12px; margin-right: 12px; flex: none;
    color: var(--brand-blue); font-size: 12px; font-weight: 700; line-height: 12px; text-align: center;
  }

  .footer-bands {
    position: absolute; left: 0; bottom: 0; width: 560px; height: 48px;
  }
</style>
</head>
<body>
<main class="canvas">

  <section class="card card--front" aria-label="Card front">
    <span class="brand-mark" aria-hidden="true"></span>
    <p class="brand-name">Toravel Project Consulting</p>
  </section>

  <section class="card card--back" aria-label="Card back">
    <span class="brand-mark" aria-hidden="true"></span>
    <p class="brand-name">Toravel Project Consulting</p>

    <div class="holder">
      <p class="holder__name">Add name</p>
      <p class="holder__role">Consultant</p>
    </div>

    <span class="divider" aria-hidden="true"></span>

    <ul class="contacts">
      <li>
        <svg class="icon" viewBox="0 0 12 12" aria-hidden="true">
          <path d="M3 1 L5 3.2 L4 4.5 C4.6 6 6 7.4 7.5 8 L8.8 7 L11 9 L9.8 10.8 C6 10.6 1.4 6 1.2 2.2 Z" fill="currentColor"/>
        </svg>
        <span>123-456-7890</span>
      </li>
      <li>
        <svg class="icon" viewBox="0 0 12 12" aria-hidden="true">
          <rect x="3" y="0.5" width="6" height="11" rx="1" fill="none" stroke="currentColor" stroke-width="1.3"/>
          <circle cx="6" cy="9.4" r="0.8" fill="currentColor"/>
        </svg>
        <span>123-456-7890</span>
      </li>
      <li>
        <span class="icon" aria-hidden="true">@</span>
        <span>info@toravelconsulting.com</span>
      </li>
    </ul>

    <svg class="footer-bands" viewBox="0 0 560 48" preserveAspectRatio="none" aria-hidden="true">
      <defs>
        <linearGradient id="greyBand" x1="0" y1="0" x2="0" y2="1">
          <stop offset="0" stop-color="var(--band-grey-light)"/>
          <stop offset="1" stop-color="var(--band-grey)"/>
        </linearGradient>
      </defs>
      <rect x="0" y="10" width="560" height="20" fill="url(#greyBand)"/>
      <path d="M300 48 C315 26 322 22 345 22 L560 22 L560 48 Z" fill="#ffffff"/>
      <path d="M308 48 C322 30 330 27 350 27 L560 27 L560 48 Z" fill="var(--band-blue)"/>
    </svg>
  </section>

</main>
</body>
</html>
```